Commercial Real Estate

We need a business card design for a new commercial real estate business that specializes in apartment building brokerage. Not individual units but the entire complex. We find and represent the owners existing buildings and well as new buyers for those buildings. The design should convey trust, integrity, knowledge and growth. It should be easily read.

Target Market(s)

40 to 65 years old

Industry/Entity Type

Real Estate

```html
<!DOCTYPE html>
<html lang="en">
<head>
<meta charset="utf-8">
<title>Tallridge Property Investments – Business Card</title>
<link rel="stylesheet" href="https://fonts.googleapis.com/css2?family=Open+Sans:wght@400;600&display=swap">
<style>
  :root {
    --bg-top: #f1f1f1;
    --bg-bottom: #d9d9d9;
    --card: #ffffff;
    --card-edge: #f4f5f5;
    --teal: #5fb0ba;
    --ink: #2b2b2b;
    --brand: #4b5c64;
    --shadow: rgba(0, 0, 0, 0.22);
  }
  * { box-sizing: border-box; margin: 0; padding: 0; }
  html, body {
    width: 1038px;
    height: 1200px;
    overflow: hidden;
  }
  body {
    background: linear-gradient(180deg, var(--bg-top), var(--bg-bottom));
    font-family: "Open Sans", Arial, sans-serif;
    color: var(--ink);
    position: relative;
  }
  .card {
    position: absolute;
    left: 119px;
    width: 800px;
    height: 459px;
    background: linear-gradient(160deg, var(--card) 55%, var(--card-edge));
    box-shadow: 0 6px 14px var(--shadow);
  }
  .card--front { top: 80px; }
  .card--back { top: 661px; }

  .holder {
    position: absolute;
    left: 74px;
    top: 104px;
  }
  .holder__name {
    font-size: 21px;
    font-weight: 600;
    color: var(--teal);
    line-height: 1.2;
  }
  .holder__title {
    font-size: 18px;
    line-height: 1.4;
  }
  .contacts {
    position: absolute;
    left: 74px;
    top: 200px;
    list-style: none;
  }
  .contacts li {
    display: flex;
    align-items: center;
    height: 29px;
    font-size: 17px;
  }
  .contacts svg {
    width: 14px;
    height: 14px;
    margin-right: 15px;
    flex: none;
  }
  .address {
    position: absolute;
    left: 74px;
    top: 348px;
    font-size: 17px;
  }
  .brand {
    position: absolute;
    left: 520px;
    top: 262px;
    width: 240px;
    display: flex;
    align-items: center;
    gap: 12px;
    color: var(--brand);
    font-weight: 600;
    font-size: 24px;
    line-height: 1.15;
  }
  .brand__square {
    width: 18px;
    height: 18px;
    background: var(--teal);
    flex: none;
  }
</style>
</head>
<body>
  <section class="card card--front" aria-label="Business card front">
    <div class="holder">
      <p class="holder__name">Dana Whitfield</p>
      <p class="holder__title">Technical Director</p>
    </div>
    <ul class="contacts">
      <li>
        <svg viewBox="0 0 14 14" aria-hidden="true"><path fill="#5fb0ba" d="M3 1l2 3-1.3 1.3a8 8 0 0 0 5 5L10 9l3 2-1.5 2.2C6.5 13 1 7.5.8 2.5z"/></svg>
        03 9000 4821
      </li>
      <li>
        <svg viewBox="0 0 14 14" aria-hidden="true"><rect x="3.5" y="1" width="7" height="12" rx="1" fill="none" stroke="#5fb0ba" stroke-width="1.4"/></svg>
        0400 318 962
      </li>
      <li>
        <svg viewBox="0 0 14 14" aria-hidden="true"><rect x="1" y="3" width="12" height="8.5" fill="none" stroke="#5fb0ba" stroke-width="1.4"/><path d="M1 3l6 5 6-5" fill="none" stroke="#5fb0ba" stroke-width="1.4"/></svg>
        dana@corvalgroup.com.au
      </li>
      <li>
        <svg viewBox="0 0 14 14" aria-hidden="true"><circle cx="7" cy="7" r="6" fill="none" stroke="#5fb0ba" stroke-width="1.3"/><path d="M1 7h12M7 1c-3 3.5-3 8.5 0 12M7 1c3 3.5 3 8.5 0 12" fill="none" stroke="#5fb0ba" stroke-width="1.1"/></svg>
        www.tallridge.com.au
      </li>
    </ul>
    <p class="address">Level 2, 18 Ardent St, Hollis, Vic 3999</p>
    <div class="brand">
      <span class="brand__square" aria-hidden="true"></span>
      <span class="brand__name">Tallridge<br>Property Investments</span>
    </div>
  </section>

  <section class="card card--back" aria-label="Business card back"></section>
</body>
</html>
```